New Business Card Design Project

We are a Nationally ranked independent premium furniture retailer, and we want to show that. I am looking for a fresh look, double sided, modern card.. Open to any ideas or designs.

Target Market(s)

Looking to hit men/women 35-50.

Industry/Entity Type

Business

Contact Information for Business Card

Looking for a clean modern look. With that being said, we are wanting to highlight some of the awards that we have received ( Corvane Best 100 and top 16 National Premium, imagines linked). Also need website on card- www.buyvelmora.com, and follow us; facebook, instagram, twitter (small thumbnails work best for those 3) Would like website, social media info, and two awards on backside with some imagery (we are a furniture, mattress and appliance business) and then logo, name, title address on front side

Colors

Designer to choose colors to be used in the design.

Requirements
Must have
• Company name, address, website, two awards, social media ques
Should not have
• cartoons

```html
<!DOCTYPE html>
<html lang="en">
<head>
<meta charset="utf-8">
<title>Velmora Home Furnishings – Business Card</title>
<link href="https://fonts.googleapis.com/css2?family=Arimo:wght@400;700&display=swap" rel="stylesheet">
<style>
  :root {
    --brand-red: #b3272b;
    --brand-blue: #2f4d9c;
    --ink: #2a2a2a;
    --paper: #ffffff;
    --backdrop: #e6e4e1;
    --rule: #cfcfcf;
  }
  * { box-sizing: border-box; margin: 0; padding: 0; }
  html, body { width: 1200px; height: 900px; overflow: hidden; }
  body {
    background: var(--backdrop);
    font-family: "Arimo", Arial, sans-serif;
    display: flex; align-items: center; justify-content: center; gap: 48px;
  }
  .card {
    width: 540px; height: 310px; position: relative; overflow: hidden;
    box-shadow: 0 6px 18px rgba(0,0,0,.18);
  }

  /* Front */
  .card-front { background: var(--paper); display: flex; }
  .front-brand {
    width: 58%; display: flex; flex-direction: column; justify-content: center; padding-left: 44px;
  }
  .brand-name { color: var(--brand-red); font-weight: 700; font-size: 52px; line-height: 1; }
  .brand-tagline { color: var(--brand-red); font-weight: 700; font-size: 21px; margin-top: 6px; }
  .front-details {
    width: 42%; border-left: 1px solid var(--rule); margin: 44px 0; padding: 8px 0 0 22px;
    color: var(--ink); font-size: 15px; line-height: 1.3;
  }
  .person-name { color: var(--brand-red); font-weight: 700; font-size: 19px; }
  .person-title { margin-bottom: 8px; }
  .contact-line { display: flex; align-items: center; gap: 7px; }
  .contact-line svg { width: 12px; height: 12px; flex: none; fill: var(--brand-red); }
  .address { margin-top: 10px; }

  /* Back */
  .card-back { background: var(--brand-red); color: var(--paper); }
  .back-website {
    position: absolute; top: 30px; width: 100%; text-align: center; font-size: 14px; letter-spacing: 1.5px;
  }
  .back-band {
    position: absolute; top: 62px; left: 0; right: 0; height: 128px; background: var(--paper);
    display: flex; align-items: center; justify-content: space-between; padding: 0 40px;
  }
  .back-band .brand-name { font-size: 40px; }
  .back-band .brand-tagline { font-size: 15px; margin-top: 4px; }
  .awards { display: flex; align-items: center; gap: 22px; }
  .award-listing { width: 118px; height: 64px; background: #dfe3ea; border-radius: 3px; }
  .award-seal { width: 60px; height: 60px; border-radius: 50%; background: var(--brand-red); }
  .back-social {
    position: absolute; top: 210px; left: 40px; right: 40px; text-align: center;
  }
  .follow-row { display: flex; align-items: center; gap: 12px; font-size: 14px; }
  .follow-row::before, .follow-row::after { content: ""; flex: 1; height: 1px; background: rgba(255,255,255,.7); }
  .social-icons { display: flex; justify-content: center; gap: 8px; margin-top: 10px; }
  .social-icons span { width: 18px; height: 18px; border-radius: 50%; background: var(--paper); }
  .bottom-rule { height: 1px; background: rgba(255,255,255,.7); margin-top: 16px; }
</style>
</head>
<body>
  <section class="card card-front" aria-label="Business card front">
    <div class="front-brand">
      <div class="brand-name">Velmora</div>
      <div class="brand-tagline">Home Furnishings</div>
    </div>
    <div class="front-details">
      <div class="person-name">DANIEL REYES</div>
      <div class="person-title">Managing Director</div>
      <div class="contact-line">
        <svg viewBox="0 0 24 24"><path d="M6.6 10.8a15 15 0 0 0 6.6 6.6l2.2-2.2a1 1 0 0 1 1-.25 11.4 11.4 0 0 0 3.6.57 1 1 0 0 1 1 1V20a1 1 0 0 1-1 1A17 17 0 0 1 3 4a1 1 0 0 1 1-1h3.5a1 1 0 0 1 1 1c0 1.25.2 2.45.57 3.57a1 1 0 0 1-.25 1z"/></svg>
        208 555 0142
      </div>
      <div class="contact-line">
        <svg viewBox="0 0 24 24"><path d="M2 5h20v14H2z M2 5l10 8 10-8" stroke="#fff" stroke-width="1.5"/></svg>
        hello@buyvelmora.com
      </div>
      <div class="contact-line">
        <svg viewBox="0 0 24 24"><circle cx="12" cy="12" r="10"/></svg>
        www.buyvelmora.com
      </div>
      <div class="address">421 Larkfield Road,<br>Boise, 83702</div>
    </div>
  </section>

  <section class="card card-back" aria-label="Business card back">
    <div class="back-website">www.buyvelmora.com</div>
    <div class="back-band">
      <div>
        <div class="brand-name">Velmora</div>
        <div class="brand-tagline">Home Furnishings</div>
      </div>
      <div class="awards">
        <div class="award-listing" role="img" aria-label="Corvane Best 100 award badge"></div>
        <div class="award-seal" role="img" aria-label="Top 16 National Premium award seal"></div>
      </div>
    </div>
    <div class="back-social">
      <div class="follow-row">Follow Us On</div>
      <div class="social-icons" aria-label="Social media links">
        <span></span><span></span><span></span>
      </div>
      <div class="bottom-rule"></div>
    </div>
  </section>
</body>
</html>
```